Home builder/contractor needs business presentation brochure

We are a custom home and remodeling firm who would like a great brochure to present to architects, designers, real estate brokers.

We are looking for additional avenues for growth potential and the ability to partner with the above types of businesses to give us an all around encompassing one stop shopping.

Target Market(s)

architects, designers, real estate brokers.

Industry/Entity Type

Real Estate

Requirements
Must have
• Please make this a tri fold and please checkout my website ridgemarkhomes.example and my houzz site as well as yelp. to gather additional information.

```html
<!DOCTYPE html>
<html lang="en">
<head>
<meta charset="utf-8">
<title>Ridgemark Homes – Tri-fold Brochure</title>
<link rel="stylesheet" href="https://fonts.googleapis.com/css2?family=Lato:wght@400;700&family=Oswald:wght@500&family=Roboto+Condensed:wght@400;700&display=swap">
<style>
  :root{
    --navy:#0c4f8e;
    --blue:#2b8fdc;
    --sky:#5db8f2;
    --pale:#8fd0f8;
    --ink:#2a2a2a;
    --paper:#ffffff;
    --stage:#e9ecef;
  }
  *{box-sizing:border-box;margin:0;padding:0}
  html,body{width:1200px;height:899px;overflow:hidden;background:var(--stage)}
  .brochure{position:relative;width:1200px;height:899px;display:flex;background:var(--paper)}
  .panel{position:relative;width:400px;height:899px;overflow:hidden}

  /* left panel */
  .panel--about{background:var(--paper)}
  .entry-photo{position:absolute;left:0;top:0;width:400px;height:420px}
  .about-swoosh{position:absolute;left:0;top:300px;width:400px;height:140px}
  .section-bar{position:absolute;left:0;width:330px;height:32px;background:var(--navy);color:#fff;
    font:700 19px/32px "Roboto Condensed",sans-serif;padding-left:32px;letter-spacing:.3px}
  .section-bar::after{content:"";position:absolute;left:330px;top:12px;width:70px;height:2px;background:var(--blue)}
  .section-bar--about{top:458px}
  .section-bar--quality{top:655px}
  .copy{position:absolute;left:32px;width:345px;font:400 13.5px/19px "Lato",sans-serif;color:var(--ink);text-align:justify}
  .copy p+p{margin-top:6px}
  .copy--about{top:502px}
  .copy--quality{top:702px}
  .footer-band{position:absolute;left:0;bottom:0;width:400px;height:26px;background:var(--navy)}

  /* middle panel */
  .panel--reach{background:linear-gradient(180deg,#2f98e6 0%,#58b6f2 55%,#7cc8f6 100%)}
  .kitchen-wash{position:absolute;inset:0;background:
      radial-gradient(ellipse 70% 40% at 50% 55%,rgba(255,255,255,.35),transparent 70%),
      linear-gradient(180deg,rgba(12,79,142,.35) 0%,rgba(12,79,142,0) 60%)}
  .reach-title{position:absolute;left:24px;top:46px;width:350px;color:#fff;
    font:700 19px/23px "Roboto Condensed",sans-serif;text-transform:uppercase}
  .reach-list{position:absolute;left:24px;top:104px;width:352px;color:#fff;
    font:400 13.5px/18px "Lato",sans-serif;text-align:justify}
  .contact{position:absolute;left:68px;top:712px;list-style:none;color:#fff;font:700 15px/26px "Lato",sans-serif}
  .contact li{display:flex;align-items:center;gap:10px}
  .contact svg{width:13px;height:13px;fill:#fff}

  /* right panel */
  .panel--cover{background:var(--paper)}
  .cover-photo{position:absolute;inset:0;width:400px;height:899px}
  .cover-swoosh{position:absolute;inset:0;width:400px;height:899px}
  .brand{position:absolute;left:0;top:205px;width:300px;display:flex;justify-content:center;align-items:center;gap:9px;
    font:400 17px/1 "Lato",sans-serif;color:#5a6b7b;letter-spacing:.6px;text-transform:uppercase}
  .brand-mark{width:12px;height:12px;background:var(--blue)}
  .tagline{position:absolute;left:58px;top:300px;color:#2d2d2d;font:700 20px/1 "Roboto Condensed",sans-serif}
  .headline{position:absolute;left:56px;top:328px;color:var(--blue);font:500 64px/66px "Oswald",sans-serif;text-transform:uppercase}
  .detail-photo{position:absolute;left:34px;top:462px;width:168px;height:168px;border-radius:50%;
    border:6px solid var(--blue);box-shadow:0 0 0 3px #fff;
    background:radial-gradient(circle at 50% 35%,#e7dccb 0%,#a67a55 45%,#5a3523 100%)}
</style>
</head>
<body>
<main class="brochure">

  <section class="panel panel--about">
    <div class="entry-photo" role="img" aria-label="Photo of a brick-framed entry with a carved wooden front door and hanging lanterns"
         style="background:linear-gradient(90deg,#8c4a34 0%,#b9745a 22%,#6b2d17 40%,#7a3a1f 60%,#b06a50 78%,#d9d6cf 100%)"></div>
    <svg class="about-swoosh" viewBox="0 0 400 140" aria-hidden="true">
      <path d="M0,40 C120,120 280,120 400,20 L400,140 L0,140 Z" fill="#fff"/>
      <path d="M0,40 C120,120 280,120 400,20" fill="none" stroke="var(--blue)" stroke-width="5"/>
      <path d="M0,58 C130,128 290,118 400,40" fill="none" stroke="var(--sky)" stroke-width="3"/>
    </svg>

    <h2 class="section-bar section-bar--about">ABOUT US</h2>
    <div class="copy copy--about">
      <p>When it comes building or remodeling your home, only the best will do. Superior quality home construction happens with experts guiding the building process.</p>
      <p>With over 30 years of building experience, General Contractor Dan Hollis of Ridgemark Homes in San Mateo has a well-earned reputation of helping homeowners realize their dream home.</p>
    </div>

    <h2 class="section-bar section-bar--quality">QUALITY, RELIABILITY, VALUE</h2>
    <div class="copy copy--quality">
      <p>At Ridgemark Homes we insist on quality building materials and superb craftsmanship with long-term performance and value utmost in our minds. Our #1 priority is to deliver superior service and continually maintain customer satisfaction. Realizing this standard of quality and value is only accomplished by being highly selective of every product and component that goes into building your home.</p>
    </div>
    <div class="footer-band"></div>
  </section>

  <section class="panel panel--reach">
    <div class="kitchen-wash" role="img" aria-label="Blue-toned photo of a kitchen island with pendant lights and dark cabinetry"></div>
    <h2 class="reach-title">Communities we serve in San Mateo County</h2>
    <p class="reach-list">San Mateo, Hillsborough, Burlingame, Millbrae, Belmont, Redwood City, Emerald Hills, Woodside, Atherton, Menlo Park, Stanford, Portola Valley, Los Altos, Los Altos Hills, Los Gatos, Foster City, Saratoga, San Carlos</p>
    <ul class="contact">
      <li><svg viewBox="0 0 24 24" aria-hidden="true"><path d="M6.6 10.8a15.1 15.1 0 0 0 6.6 6.6l2.2-2.2c.3-.3.7-.4 1-.2 1.1.4 2.3.6 3.6.6.6 0 1 .4 1 1V20c0 .6-.4 1-1 1A17 17 0 0 1 3 4c0-.6.4-1 1-1h3.5c.6 0 1 .4 1 1 0 1.3.2 2.5.6 3.6.1.3 0 .7-.2 1z"/></svg>650-555-0142</li>
      <li><svg viewBox="0 0 24 24" aria-hidden="true"><path d="M2 5h20v14H2z M2 5l10 8 10-8" /></svg>dan@ridgemarkhomes.example</li>
      <li><svg viewBox="0 0 24 24" aria-hidden="true"><path d="M12 2a10 10 0 1 0 0 20 10 10 0 0 0 0-20zm0 2c1 1.3 1.8 3.4 2 6h-4c.2-2.6 1-4.7 2-6zm-2 8h4c-.2 2.6-1 4.7-2 6-1-1.3-1.8-3.4-2-6zm-5.9 0h3.9c.1 2.3.6 4.3 1.4 5.7A8 8 0 0 1 4.1 12zm0-2a8 8 0 0 1 5.3-5.7C8.6 5.7 8.1 7.7 8 10zm11.9 2h3.9a8 8 0 0 1-5.3 5.7c.8-1.4 1.3-3.4 1.4-5.7zm0-2c-.1-2.3-.6-4.3-1.4-5.7a8 8 0 0 1 5.3 5.7z"/></svg>www.ridgemarkhomes.example</li>
    </ul>
  </section>

  <section class="panel panel--cover">
    <svg class="cover-photo" viewBox="0 0 400 899" role="img" aria-label="Photo of a bright kitchen with white cabinets, a range and a stainless refrigerator">
      <defs>
        <linearGradient id="kitchenTones" x1="0" y1="0" x2="1" y2="1">
          <stop offset="0" stop-color="#efe9df"/>
          <stop offset=".5" stop-color="#cfc2ae"/>
          <stop offset="1" stop-color="#8a4a2a"/>
        </linearGradient>
      </defs>
      <path d="M400,40 C385,360 210,600 40,899 L400,899 Z" fill="url(#kitchenTones)"/>
    </svg>
    <svg class="cover-swoosh" viewBox="0 0 400 899" aria-hidden="true">
      <path d="M300,0 C410,120 400,420 200,620 C120,700 60,800 30,899" fill="none" stroke="var(--sky)" stroke-width="6"/>
      <path d="M340,0 C430,140 420,400 240,600" fill="none" stroke="var(--navy)" stroke-width="10"/>
      <path d="M370,0 C420,60 410,200 400,260" fill="none" stroke="var(--blue)" stroke-width="14"/>
      <path d="M60,899 C120,760 200,660 290,560" fill="none" stroke="var(--blue)" stroke-width="8"/>
    </svg>

    <div class="brand"><span class="brand-mark"></span>Ridgemark Homes</div>
    <p class="tagline">BEAUTIFUL HOMES</p>
    <h1 class="headline">Built to<br>Last</h1>
    <div class="detail-photo" role="img" aria-label="Round photo of a kitchen with dark wood cabinets and a center island"></div>
  </section>

</main>
</body>
</html>
```